The Copper Hour ebook cover for Desmond Okafor Whitley

I need an ebook cover/jpeg that depicts a Middle-Eastern desert and sky. The cover must be very elegant and very austere, the simpler the better.
Toward the top, the text will read: The Copper Hour
Directly below the title will read: Corvin Teague
The dimensions for the cover should be 2560 pixels (height) and 1600 pixels (width.)

Target Market(s)

Readers of serious magical realism and/or fantasy literature with a serious literary element.

Font styles to use
Serif

Requirements
Must have
• My ebook cover MUST be a painting or illustration depicting a very austere Middle-Eastern desert and desert sky. Must be elegant and austere. The lettering of the title and author name must blend in beautifully with the image--just like fine books in a bookstore. Title must appear at the top: The Copper Hour. The author's name must appear below title and read: Corvin Teague. Dimensions must be 2560 pixels (height) by 1600 pixels (width)
Nice to have
• A very austere desert on the bottom and a sad elegant sky above.
Should not have
• My ebook cover should not have a spine or a back. I just need an ebook cover of the dimensions stated above.

```html
<!DOCTYPE html>
<html lang="en">
<head>
<meta charset="utf-8">
<title>The Copper Hour — Corvin Teague</title>
<link href="https://fonts.googleapis.com/css2?family=Cinzel:wght@400;500&display=swap" rel="stylesheet">
<style>
  :root {
    --page-bg: #ffffff;
    --sky-top: #4951a4;
    --sky-mid: #6d72b8;
    --sky-haze: #b9bbe0;
    --sky-pale: #f3f2f8;
    --dune-light: #f5b53a;
    --dune-mid: #e59a22;
    --dune-shadow: #a9561a;
    --dune-deep: #7a3b14;
    --band: #833c1c;
    --author: #f6d68e;
    --title: #ffffff;
    --rule: rgba(255, 255, 255, 0.75);
  }
  * { margin: 0; padding: 0; box-sizing: border-box; }
  html, body {
    width: 1200px;
    height: 960px;
    overflow: hidden;
    background: var(--page-bg);
  }
  .canvas {
    position: relative;
    width: 1200px;
    height: 960px;
  }
  .cover {
    position: absolute;
    left: 375px;
    top: 120px;
    width: 450px;
    height: 720px;
    overflow: hidden;
    font-family: "Cinzel", "Trajan Pro", serif;
  }
  .cover-art {
    position: absolute;
    inset: 0;
    background:
      linear-gradient(180deg,
        var(--sky-top) 0%,
        var(--sky-mid) 20%,
        var(--sky-haze) 36%,
        var(--sky-pale) 45%,
        var(--dune-mid) 50%,
        var(--dune-light) 62%,
        var(--dune-shadow) 76%,
        var(--dune-mid) 86%,
        var(--dune-light) 100%);
  }
  .title-block {
    position: absolute;
    top: 60px;
    left: 0;
    width: 100%;
    text-align: center;
    color: var(--title);
    text-shadow: 0 2px 6px rgba(40, 40, 90, 0.35);
  }
  .title-kicker {
    position: relative;
    display: flex;
    align-items: center;
    justify-content: center;
    gap: 14px;
    font-size: 21px;
    letter-spacing: 1px;
    line-height: 1;
  }
  .title-kicker .rule {
    display: block;
    width: 103px;
    height: 1px;
    background: var(--rule);
  }
  .title-main {
    font-weight: 400;
    font-size: 56px;
    line-height: 54px;
    letter-spacing: 1px;
    margin-top: 6px;
  }
  .title-rule {
    width: 278px;
    height: 1px;
    background: var(--rule);
    margin: 14px auto 0;
  }
  .author-band {
    position: absolute;
    left: 0;
    top: 654px;
    width: 100%;
    height: 31px;
    background: var(--band);
    color: var(--author);
    display: flex;
    align-items: center;
    justify-content: center;
    font-size: 20px;
    letter-spacing: 1px;
  }
</style>
</head>
<body>
  <div class="canvas">
    <div class="cover">
      <div class="cover-art" role="img" aria-label="Photograph of tall golden desert dunes with rippled sand in front, under a deep blue sky fading to pale haze at the horizon"></div>
      <div class="title-block">
        <div class="title-kicker"><span class="rule"></span>THE<span class="rule"></span></div>
        <h1 class="title-main">COPPER<br>HOUR</h1>
        <div class="title-rule"></div>
      </div>
      <div class="author-band">CORVIN TEAGUE</div>
    </div>
  </div>
</body>
</html>
```